skincare creams for tired moms

I need a package and a logo design for a skincare company based in California called Lumen Petal. I make day and night cream, under eye cream, and body lotion. The first product I plan to launch is an under eye cream. It does not have to be in these colors but I do teals, greens, black, and cobalt blue.

The package is going to either be in a box or a bag. Either way I go it will be like a gift box or bag. The design should make the person feel like they are getting something special and luxurious just for them.

I have small kids and it is really difficult to find a chunk of time to myself to update or review.

Target Market(s)

mainly first time moms. I am making an under eye cream that does not use retinol but is still powerful enough to get rid of bags and dark circles.

Industry/Entity Type

Cosmetics

Logo Text

The package and logo should incorporate the name Lumen Petal.

Font styles to use
Decorative
Script

Colors

Designer to choose colors to be used in the design.

Requirements
Nice to have
• maybe focus more on Petal instead of Lumen. Also incorporate plants or flowers
Should not have
• not a huge fan of pink

```html
<!DOCTYPE html>
<html lang="en">
<head>
<meta charset="utf-8">
<title>Lumen Petal — Packaging line</title>
<link rel="stylesheet" href="https://fonts.googleapis.com/css2?family=Karla:wght@300;400;600;700&family=Kaushan+Script&display=swap">
<style>
  :root {
    --paper: #ffffff;
    --ink: #000000;
    --title: #1a1a1a;
    --white: #ffffff;
    --mint: #9ddecb;
    --mint-soft: #c4ece0;
    --teal: #1ecfcb;
    --teal-soft: #6fe2df;
    --cobalt: #150b8c;
    --cobalt-soft: #3a30b8;
    --cobalt-text: #7b72f2;
    --sky: #b3d7e8;
    --sky-soft: #d6eaf3;
    --sans: "Karla", Arial, sans-serif;
    --script: "Kaushan Script", cursive;
  }
  * { box-sizing: border-box; margin: 0; padding: 0; }
  html, body { width: 1200px; height: 1200px; overflow: hidden; background: var(--paper); }
  .board { position: relative; width: 1200px; height: 1200px; font-family: var(--sans); }
  .board-title {
    position: absolute; left: 155px; top: 184px;
    font-family: var(--sans); font-weight: 300; font-size: 29px; color: var(--title); letter-spacing: 0.3px;
  }
  .pack { position: absolute; }
  .pack-pattern { position: absolute; inset: 0; }
  .label { position: absolute; background: var(--ink); color: var(--white); text-align: center; }
  .brand-mark { display: block; border-radius: 50%; margin: 0 auto; }
  .brand-name { font-weight: 700; color: var(--white); white-space: nowrap; }
  .tagline, .benefit { font-weight: 600; white-space: nowrap; }
  .product-name { font-family: var(--script); color: var(--white); white-space: nowrap; line-height: 1; }

  /* body lotion */
  .pack--lotion { left: 156px; top: 283px; width: 331px; height: 648px; }
  .pack--lotion .pack-pattern {
    background:
      repeating-linear-gradient(90deg, transparent 0 40px, rgba(255,255,255,0.22) 40px 56px),
      linear-gradient(180deg, var(--mint) 0%, var(--mint-soft) 100%);
  }
  .pack--lotion .label--brand { left: 47px; top: 0; width: 236px; height: 236px; padding-top: 32px; }
  .pack--lotion .brand-mark { width: 118px; height: 118px; background: var(--mint); }
  .pack--lotion .brand-name { font-size: 25px; margin-top: 33px; }
  .pack--lotion .label--product { left: 47px; top: 250px; width: 236px; height: 179px; padding-top: 18px; }
  .pack--lotion .tagline, .pack--lotion .benefit { font-size: 9.5px; color: var(--mint); }
  .pack--lotion .product-name { font-size: 46px; margin: 30px 0 40px; }

  /* day & night cream */
  .pack--jar { width: 305px; height: 305px; }
  .pack--day { left: 524px; top: 285px; }
  .pack--night { left: 527px; top: 626px; }
  .pack--day .pack-pattern {
    background:
      repeating-linear-gradient(90deg, transparent 0 30px, rgba(255,255,255,0.25) 30px 44px),
      linear-gradient(180deg, var(--teal) 0%, var(--teal-soft) 100%);
  }
  .pack--night .pack-pattern {
    background:
      repeating-linear-gradient(90deg, transparent 0 30px, rgba(255,255,255,0.18) 30px 44px),
      linear-gradient(180deg, var(--cobalt) 0%, var(--cobalt-soft) 100%);
  }
  .pack--jar .label--brand { left: 67px; top: 0; width: 172px; height: 171px; padding-top: 24px; }
  .pack--jar .brand-mark { width: 96px; height: 96px; }
  .pack--day .brand-mark { background: var(--teal); }
  .pack--night .brand-mark { background: var(--cobalt-text); }
  .pack--jar .brand-name { font-size: 19px; margin-top: 17px; }
  .pack--jar .label--product { left: 67px; top: 182px; width: 172px; height: 88px; padding-top: 8px; }
  .pack--jar .tagline, .pack--jar .benefit { font-size: 7.5px; }
  .pack--day .tagline, .pack--day .benefit { color: var(--teal); }
  .pack--night .tagline, .pack--night .benefit { color: var(--cobalt-text); }
  .pack--jar .product-name { font-size: 30px; margin: 9px 0 9px; }

  /* under-eye cream */
  .pack--eye { left: 874px; top: 281px; width: 178px; height: 655px; }
  .pack--eye .pack-pattern {
    background:
      repeating-linear-gradient(90deg, transparent 0 28px, rgba(255,255,255,0.3) 28px 42px),
      linear-gradient(180deg, var(--sky) 0%, var(--sky-soft) 100%);
  }
  .pack--eye .label--brand { left: 31px; top: 0; width: 108px; height: 107px; }
  .pack--eye .brand-name {
    position: absolute; left: 25px; top: 19px; font-size: 11px;
    transform-origin: top left; transform: rotate(90deg);
  }
  .pack--eye .brand-mark {
    position: absolute; left: 33px; top: 20px; width: 64px; height: 64px; background: var(--sky);
  }
  .pack--eye .label--product { left: 31px; top: 120px; width: 108px; height: 282px; }
  .eye-rotated {
    position: absolute; left: 0; top: 0; width: 282px; height: 108px;
    transform-origin: top left; transform: translateX(108px) rotate(90deg);
    padding-top: 12px; text-align: center;
  }
  .pack--eye .tagline { font-size: 9px; color: var(--sky); }
  .pack--eye .product-name { font-size: 37px; margin: 8px 0 9px; }
  .pack--eye .benefit { font-size: 9px; color: var(--sky); }
</style>
</head>
<body>
<main class="board">
  <h1 class="board-title">Packaging line</h1>

  <section class="pack pack--lotion">
    <div class="pack-pattern" role="img" aria-label="Repeating white leaf sprig pattern on mint green"></div>
    <div class="label label--brand">
      <span class="brand-mark"></span>
      <p class="brand-name">Lumen Petal</p>
    </div>
    <div class="label label--product">
      <p class="tagline">Amazing cosmetics for amazing mums.</p>
      <p class="product-name">body lotion</p>
      <p class="benefit">Soothing, nourishing &amp; intensely moisturizing.</p>
    </div>
  </section>

  <section class="pack pack--jar pack--day">
    <div class="pack-pattern" role="img" aria-label="Repeating white leaf sprig pattern on bright teal"></div>
    <div class="label label--brand">
      <span class="brand-mark"></span>
      <p class="brand-name">Lumen Petal</p>
    </div>
    <div class="label label--product">
      <p class="tagline">Amazing cosmetics for amazing mums.</p>
      <p class="product-name">day cream</p>
      <p class="benefit">Light, moisturizing &amp; energizing.</p>
    </div>
  </section>

  <section class="pack pack--jar pack--night">
    <div class="pack-pattern" role="img" aria-label="Repeating white leaf sprig pattern on cobalt blue"></div>
    <div class="label label--brand">
      <span class="brand-mark"></span>
      <p class="brand-name">Lumen Petal</p>
    </div>
    <div class="label label--product">
      <p class="tagline">Amazing cosmetics for amazing mums.</p>
      <p class="product-name">night cream</p>
      <p class="benefit">Rich, nourishing &amp; revitalizing.</p>
    </div>
  </section>

  <section class="pack pack--eye">
    <div class="pack-pattern" role="img" aria-label="Repeating white leaf sprig pattern on pale sky blue"></div>
    <div class="label label--brand">
      <p class="brand-name">Lumen Petal</p>
      <span class="brand-mark"></span>
    </div>
    <div class="label label--product">
      <div class="eye-rotated">
        <p class="tagline">Amazing cosmetics for amazing mums.</p>
        <p class="product-name">under-eye cream</p>
        <p class="benefit">Diminishes eye bags &amp; dark circles. Without retinol.</p>
      </div>
    </div>
  </section>
</main>
</body>
</html>
```